Website for Brisbeck Current Glide

Require a website for a river float in the City of Edmonton. Located on North Saskatchewan River. Will need to be a coded website with incorporated booking system through Fare Harbor software.

Pages include
Home
Pricing
About
FAQ
Contact

Brisbeck Current Glide is an activity based business that will have customers floating down the North Saskatchewan river in Edmonton AB. The site will have all information needed and a full reservation system. The project was launched to provide people in the Edmonton area a favorite summer activity.

Here are similar websites to reference what our business will be doing and what we are looking for.

mellowbendcanoehire.example
pinegulchloopers.example

Target Market(s)

Families, Groups, Individuals, Anyone who wants to explore the river

Industry/Entity Type

Activities based business/ Outdoor recreational/ River Float

Coding

Coded - Design and coding required

Number of Pages Required

5+ page

Colors
0054AA
0677BA
7BADD7
CADEEF
E8F1F8
F0912C
F2A743
F7CA91
FBE8D2
FDF5EE

```html
<!DOCTYPE html>
<html lang="en">
<head>
<meta charset="utf-8">
<title>Brisbeck Current Glide</title>
<link href="https://fonts.googleapis.com/css2?family=Poppins:wght@300;400;500;600;700;800&display=swap" rel="stylesheet">
<style>
:root{
  --navy:#173d80;
  --navy-deep:#0f2f66;
  --cyan:#48c1e6;
  --cyan-soft:#7fd3ee;
  --orange:#e05a2e;
  --coral:#e06a45;
  --ice:#e8f6fb;
  --white:#ffffff;
  --text:#6b6b6b;
  --ink:#2b2b2b;
}
*{margin:0;padding:0;box-sizing:border-box}
html,body{width:1200px;height:2966px;overflow:hidden;background:var(--ice)}
body{font-family:'Poppins',sans-serif;color:var(--text)}
.page{position:relative;width:1200px;height:2966px;overflow:hidden;background:var(--ice)}
.abs{position:absolute}
.btn{position:absolute;display:flex;align-items:center;justify-content:center;border-radius:20px;background:var(--orange);color:var(--white);font-size:13px;font-weight:400;letter-spacing:.3px}
.btn-ghost{background:var(--white);color:var(--orange);border:1px solid var(--orange)}

/* header */
.site-header{position:absolute;left:0;top:0;width:1200px;height:61px;background:var(--white);z-index:5}
.brand-badge{position:absolute;left:60px;top:3px;width:104px;height:104px;border-radius:50%;background:var(--white);z-index:6;display:flex;align-items:center;justify-content:center;text-align:center;color:var(--navy);font-weight:700;font-size:12px;line-height:1.15}
.nav{position:absolute;top:20px;left:625px;display:flex;gap:0;font-size:13px;color:var(--ink)}
.nav span{position:absolute;white-space:nowrap}
.nav .active{color:var(--cyan)}

/* hero */
.hero-photo{position:absolute;left:0;top:61px;width:1200px;height:640px;background:linear-gradient(180deg,#1f4cc0 0%,#3d6fd0 22%,#8aa6c9 36%,#55714f 44%,#3f6a3e 50%,#2f72b8 56%,#2a76c6 75%,#2a6fc0 100%)}
.hero-title{position:absolute;top:272px;left:0;width:1200px;text-align:center;color:var(--white);font-weight:800;font-size:36px;letter-spacing:.5px}
.hero-sub{position:absolute;top:320px;left:0;width:1200px;text-align:center;color:var(--white);font-size:13px;font-weight:300}
.hero-btn{left:542px;top:375px;width:114px;height:37px;border:2px solid var(--white)}
.slide-dot{position:absolute;left:1125px;width:8px;height:8px;border-radius:50%;background:var(--white)}
.slide-dot.current{background:var(--cyan)}

/* welcome */
.welcome-photo{position:absolute;border-radius:22px}
.welcome-title{position:absolute;left:558px;top:738px;font-size:26px;font-weight:800;white-space:nowrap;color:var(--navy)}
.welcome-title .lead{color:var(--cyan)}
.welcome-copy{position:absolute;left:558px;top:788px;width:486px;font-size:13.5px;font-weight:300;line-height:22.5px;color:var(--text)}
.welcome-copy p+p{margin-top:7px}

/* pricing */
.pricing-title{position:absolute;top:1245px;left:0;width:1200px;text-align:center;color:var(--white);font-size:26px;font-weight:800}
.price-frame{position:absolute;left:300px;top:1304px;width:530px;height:326px;border:1px solid var(--cyan-soft);border-radius:14px}
.price-card{position:absolute;left:307px;top:1309px;width:516px;height:317px;background:var(--white);border-radius:12px}
.price-card h3{position:absolute;left:38px;top:22px;font-size:13px;font-weight:700;color:var(--navy-deep)}
.price-card .intro{position:absolute;left:38px;top:47px;width:345px;font-size:13.5px;line-height:22px;color:var(--ink);font-weight:300}
.price-list{position:absolute;list-style:none;font-size:13.5px;color:var(--ink);font-weight:300}
.price-list li{position:absolute;white-space:nowrap;padding-left:16px}
.price-list li::before{content:"";position:absolute;left:0;top:8px;width:6px;height:6px;border-radius:50%;background:var(--cyan)}
.price-badge{position:absolute;left:859px;top:1290px;width:56px;height:56px;border-radius:50%;background:var(--orange);border:2px solid var(--cyan-soft);color:var(--white);font-size:15px;font-weight:500;line-height:20px;text-align:center;padding-top:6px}

/* faq */
.faq-title{position:absolute;top:1748px;left:0;width:1200px;text-align:center;color:var(--cyan);font-size:26px;font-weight:800}
.faq-item{position:absolute;width:412px;height:39px;background:var(--white);border:1px solid #8fa9c9;border-radius:3px;font-size:13.5px;color:var(--ink);font-weight:300;padding:8px 0 0 12px}
.faq-item::after{content:"+";position:absolute;right:10px;top:10px;width:18px;height:18px;border-radius:50%;background:var(--cyan-soft);color:var(--white);font-size:16px;font-weight:500;line-height:17px;text-align:center}

/* contact */
.contact-title{position:absolute;top:2346px;left:0;width:1200px;text-align:center;color:var(--white);font-size:26px;font-weight:800}
.contact-lead{position:absolute;left:231px;top:2402px;font-size:22px;font-weight:600;color:var(--cyan)}
.contact-row{position:absolute;left:233px;display:flex;align-items:center;gap:14px;color:var(--white);font-size:16px;font-weight:300}
.contact-row.strong{font-weight:600}
.social{position:absolute;width:40px;height:40px;border-radius:50%;background:var(--white);color:var(--navy);font-size:10px;font-weight:600;display:flex;align-items:center;justify-content:center;border:2px solid var(--navy)}

/* footer */
.site-footer{position:absolute;left:0;top:2686px;width:1200px;height:280px;background:var(--navy-deep)}
.footer-brand{position:absolute;left:60px;top:70px;width:215px;color:var(--white);font-size:27px;font-weight:700;line-height:32px;text-align:center}
.footer-head{position:absolute;top:40px;font-size:13px;font-weight:500;color:var(--cyan);letter-spacing:.5px}
.footer-nav{position:absolute;left:335px;list-style:none;color:var(--white);font-size:11.5px;font-weight:300}
.footer-nav li{position:absolute;left:0;white-space:nowrap;padding-left:20px}
.footer-nav li::before{content:"";position:absolute;left:0;top:6px;width:6px;height:6px;border-radius:50%;background:var(--cyan)}
.open-badge{position:absolute;left:637px;top:32px;width:80px;height:80px;border-radius:50%;background:var(--orange);border:3px solid var(--cyan-soft);color:var(--white);text-align:center;font-size:10px;font-weight:600;line-height:13px;padding-top:18px}
.open-badge b{font-size:22px;font-weight:600}
.signup-label{position:absolute;left:613px;top:139px;font-size:12px;color:var(--white);font-weight:300}
.signup{position:absolute;left:611px;top:170px;width:229px;height:30px;border-radius:15px;background:var(--white);border:1px solid var(--cyan)}
.signup .field{position:absolute;left:11px;top:7px;font-size:11px;color:#555}
.signup .go{position:absolute;right:2px;top:2px;width:82px;height:24px;border-radius:12px;background:var(--orange);color:var(--white);font-size:11px;display:flex;align-items:center;justify-content:center}
.footer-contact{position:absolute;left:890px;display:flex;align-items:center;gap:12px;color:var(--white);font-size:12px;font-weight:300}
.footer-social{position:absolute;top:190px;width:30px;height:30px;border-radius:50%;background:var(--white);color:var(--navy);font-size:8px;font-weight:600;display:flex;align-items:center;justify-content:center;border:2px solid var(--cyan)}
.footer-rule{position:absolute;left:0;top:245px;width:1200px;height:1px;background:rgba(255,255,255,.25)}
.copyright{position:absolute;top:253px;left:0;width:1200px;text-align:center;color:var(--white);font-size:11.5px;font-weight:300}
</style>
</head>
<body>
<div class="page">

  <!-- hero -->
  <div class="hero-photo" role="img" aria-label="City skyline above a wide blue river with green wooded banks and a bridge"></div>

  <svg class="abs" style="left:0;top:0" width="1200" height="2966" viewBox="0 0 1200 2966" aria-hidden="true">
    <path d="M0,595 C80,555 150,565 230,595 C340,635 430,660 530,630 C650,590 710,515 830,485 C930,460 1010,455 1080,465 C1130,472 1170,462 1200,440 L1200,720 L0,720 Z" fill="#48c1e6"/>
    <path d="M0,612 C90,575 150,588 232,622 C340,664 430,690 532,658 C650,620 712,545 832,515 C930,492 1020,492 1088,505 C1140,515 1176,512 1200,500 L1200,720 L0,720 Z" fill="#e8f6fb"/>
    <path d="M1200,440 C1185,470 1160,490 1130,520 L1200,520 Z" fill="#48c1e6"/>
    <circle cx="1026" cy="546" r="20" fill="#48c1e6"/><circle cx="1026" cy="546" r="8" fill="#173d80"/>
    <circle cx="1060" cy="578" r="14" fill="#48c1e6"/><circle cx="1060" cy="578" r="5" fill="#173d80"/>
    <circle cx="51" cy="644" r="14" fill="#48c1e6"/><circle cx="51" cy="644" r="6" fill="#173d80"/>
    <circle cx="83" cy="678" r="20" fill="#48c1e6"/><circle cx="83" cy="678" r="8" fill="#173d80"/>
    <path d="M1129,238 L1129,222 M1124,228 L1129,222 L1134,228" stroke="#fff" stroke-width="1.5" fill="none"/>
    <path d="M1129,310 L1129,326 M1124,320 L1129,326 L1134,320" stroke="#fff" stroke-width="1.5" fill="none"/>

    <!-- pricing band -->
    <path d="M0,1158 C300,1125 640,1118 900,1138 C1040,1150 1130,1175 1200,1200 L1200,1700 L0,1700 Z" fill="#2c64ad"/>
    <path d="M0,1168 C300,1142 620,1132 870,1152 C1010,1164 1120,1192 1200,1218 L1200,1700 L0,1700 Z" fill="url(#pricingBg)"/>
    <defs>
      <linearGradient id="pricingBg" x1="0" y1="0" x2="0" y2="1">
        <stop offset="0" stop-color="#1a4a8e"/><stop offset=".5" stop-color="#1f5598"/><stop offset="1" stop-color="#174785"/>
      </linearGradient>
      <linearGradient id="contactPhoto" x1="0" y1="0" x2="0" y2="1">
        <stop offset="0" stop-color="#4f6a3a"/><stop offset=".45" stop-color="#6f7f55"/><stop offset="1" stop-color="#4d6b78"/>
      </linearGradient>
      <linearGradient id="raftPhoto" x1="0" y1="0" x2="0" y2="1">
        <stop offset="0" stop-color="#4e7a3a"/><stop offset=".5" stop-color="#7e9a8a"/><stop offset="1" stop-color="#c9b23a"/>
      </linearGradient>
    </defs>

    <!-- contact band -->
    <path d="M0,2243 C250,2292 500,2318 700,2310 C900,2302 1050,2282 1200,2270 L1200,2690 L0,2690 Z" fill="#e06a45"/>
    <path d="M700,2600 C690,2450 780,2362 888,2362 C1000,2362 1085,2450 1078,2590 C1050,2612 1020,2640 985,2625 C950,2610 930,2655 895,2650 C860,2645 840,2625 800,2630 C760,2640 735,2640 700,2600 Z" fill="url(#contactPhoto)" role="img" aria-label="Child relaxing on an inflatable ring in a green river"/>
    <path d="M715,2625 C745,2650 770,2645 805,2638 C845,2632 862,2655 898,2660 C935,2662 955,2620 988,2635 C1020,2650 1050,2620 1078,2598" stroke="#48c1e6" stroke-width="3" fill="none"/>
  </svg>

  <header class="site-header">
    <nav class="nav">
      <span class="active" style="left:0">HOME</span>
      <span style="left:68px">PRICING</span>
      <span style="left:160px">ABOUT</span>
      <span style="left:238px">FAQ</span>
      <span style="left:301px">CONTACT</span>
    </nav>
    <div class="btn" style="left:1025px;top:13px;width:113px;height:35px">BOOK NOW</div>
  </header>
  <div class="brand-badge">Brisbeck<br>Current<br>Glide</div>

  <h1 class="hero-title">BRISBECK CURRENT GLIDE</h1>
  <p class="hero-sub">Float the North Saskatchewan through downtown Edmonton</p>
  <div class="btn hero-btn">BOOK NOW</div>
  <span class="slide-dot" style="top:247px"></span>
  <span class="slide-dot current" style="top:270px"></span>
  <span class="slide-dot" style="top:292px"></span>

  <!-- welcome -->
  <div class="welcome-photo" style="left:60px;top:754px;width:231px;height:248px;background:linear-gradient(180deg,#7d97a8,#4b8ec0 45%,#1e7fd0)" role="img" aria-label="Blue inflatable river tube floating on calm water"></div>
  <div class="welcome-photo" style="left:249px;top:821px;width:231px;height:249px;background:linear-gradient(180deg,#b89a80,#e0a060 40%,#6b5a4a 70%,#3a3a3e)" role="img" aria-label="Boats on a river at sunset with city towers"></div>
  <h2 class="welcome-title"><span class="lead">WELCOME</span> BRISBECK CURRENT GLIDE</h2>
  <div class="welcome-copy">
    <p>Float the North Saskatchewan through downtown Edmonton Edmonton's Best Summer Activity.We provide the lifejacket, paddle, river tube and shuttle service. You just have to show up.Brisbeck Current Glide was launched to provide people in the Edmonton area a favorite summeractivity. Nothing is better on a hot summer day, than spending it on the river and seeing Edmonton from a new perspective.</p>
    <p>Our priority is to make sure everyone has a safe and fun time on the river. Safety demonstrations are provided and staff are available to assist in any way. Whether you are a family with children, larger group or just want a relaxing way to explore the river, this is a must try activity.</p>
  </div>
  <div class="btn" style="left:558px;top:1047px;width:109px;height:32px">BOOK NOW</div>

  <!-- pricing -->
  <h2 class="pricing-title">OUR PRICING</h2>
  <div class="price-frame"></div>
  <div class="price-card">
    <h3>TUBE AND SHUTTLE</h3>
    <p class="intro">We keep our pricing simple and include everything you need:<br>Premium comfort float tube with backrest and cup holder</p>
    <ul class="price-list" style="left:35px;top:140px">
      <li style="top:0">Lifejacket</li>
      <li style="top:26px">Safety training</li>
      <li style="top:50px">Staff assistance</li>
      <li style="top:77px">Unlimited Fun!</li>
      <li style="top:0;left:138px">Paddle</li>
      <li style="top:26px;left:138px">Round trip shuttle service</li>
      <li style="top:50px;left:138px">Parking</li>
      <li style="top:77px;left:138px">Group of 10 or more?</li>
    </ul>
    <div class="btn" style="left:38px;top:256px;width:109px;height:31px">BOOK NOW</div>
    <div class="btn btn-ghost" style="left:180px;top:256px;width:118px;height:31px">CONTACT US</div>
  </div>
  <svg class="abs" style="left:705px;top:1295px" width="232" height="232" viewBox="0 0 232 232">
    <circle cx="116" cy="116" r="113" fill="#fff" stroke="#7fd3ee" stroke-width="2"/>
    <circle cx="116" cy="116" r="106" fill="url(#raftPhoto)" role="img" aria-label="Group in life jackets paddling a yellow raft through white water"/>
  </svg>
  <div class="price-badge">$<br>15</div>

  <!-- faq -->
  <h2 class="faq-title">FAQ</h2>
  <div class="faq-item" style="left:172px;top:1808px">How do I reserve my float?</div>
  <div class="faq-item" style="left:172px;top:1863px">What is included?</div>
  <div class="faq-item" style="left:172px;top:1916px">Where are you located?</div>
  <div class="faq-item" style="left:172px;top:1969px">Where should I park?</div>
  <div class="faq-item" style="left:172px;top:2022px">What happens if I miss my shuttle?</div>
  <div class="faq-item" style="left:172px;top:2075px">Are lifejackets required?</div>
  <div class="faq-item" style="left:172px;top:2127px">Is the North Saskatchewan River safe to float down?</div>
  <div class="faq-item" style="left:172px;top:2180px">What happens if I miss the exit point?</div>
  <div class="faq-item" style="left:615px;top:1808px">What safety information should I know?</div>
  <div class="faq-item" style="left:615px;top:1863px">What should I bring?</div>
  <div class="faq-item" style="left:615px;top:1916px">How do I reserve my float?</div>
  <div class="faq-item" style="left:615px;top:1969px">How long does the trip take?</div>
  <div class="faq-item" style="left:615px;top:2022px">How do I complete the waiver?</div>
  <div class="faq-item" style="left:615px;top:2075px">What do I do if there is bad weather on the day...</div>
  <div class="faq-item" style="left:615px;top:2127px">What are the terms and conditions?</div>
  <div class="faq-item" style="left:615px;top:2180px">What is your cancellation policy?</div>

  <!-- contact -->
  <h2 class="contact-title">CONTACT US</h2>
  <p class="contact-lead">We'd love to hear from you!</p>
  <div class="contact-row strong" style="top:2458px">
    <svg width="24" height="24" viewBox="0 0 24 24" fill="none" stroke="#173d80" stroke-width="1.5"><path d="M5 3 L9 3 L10.5 8 L8 9.5 C9.5 12.5 11.5 14.5 14.5 16 L16 13.5 L21 15 L21 19 C21 20 20 21 19 21 C10 20.5 3.5 14 3 5 C3 4 4 3 5 3 Z"/></svg>
    <span>780XXXXXXX</span>
  </div>
  <div class="contact-row" style="top:2496px">
    <svg width="24" height="24" viewBox="0 0 24 24" fill="none" stroke="#173d80" stroke-width="1.5"><rect x="2.5" y="5" width="19" height="14"/><path d="M2.5 5 L12 13 L21.5 5"/></svg>
    <span>info@brisbeckcurrentglide.example</span>
  </div>
  <div class="contact-row" style="top:2534px">
    <svg width="24" height="24" viewBox="0 0 24 24" fill="none" stroke="#173d80" stroke-width="1.5"><path d="M12 21 C12 21 5 14 5 9 A7 7 0 0 1 19 9 C19 14 12 21 12 21 Z"/><circle cx="12" cy="9" r="2.5"/><path d="M6 21 L18 21"/></svg>
    <span>4120 Ferrow Lane NW, Edmonton, AB</span>
  </div>
  <div class="social" style="left:237px;top:2589px">Pix</div>
  <div class="social" style="left:309px;top:2589px">Feed</div>
  <div class="social" style="left:382px;top:2589px">Rate</div>

  <!-- footer -->
  <footer class="site-footer">
    <div class="abs" style="left:137px;top:22px;width:60px;height:60px;border-radius:50%;background:var(--cyan)"></div>
    <div class="footer-brand" style="top:95px">BRISBECK CURRENT GLIDE</div>

    <div class="footer-head" style="left:335px">NAVIGATION</div>
    <ul class="footer-nav" style="top:70px">
      <li style="top:0">HOME</li>
      <li style="top:30px">PRICING</li>
      <li style="top:62px">ABOUT</li>
      <li style="top:94px">FAQ</li>
      <li style="top:124px">CONTACT</li>
    </ul>

    <div class="open-badge">OPEN <b>7</b> DAYS<br>A WEEK</div>
    <p class="signup-label">Sign Up For Our Mailing List</p>
    <div class="signup"><span class="field">E-MAIL</span><span class="go">SUBSCRIBE</span></div>

    <div class="footer-head" style="left:890px">CONTACT US</div>
    <div class="footer-contact" style="top:72px">
      <svg width="18" height="18" viewBox="0 0 24 24" fill="none" stroke="#fff" stroke-width="1.5"><path d="M5 3 L9 3 L10.5 8 L8 9.5 C9.5 12.5 11.5 14.5 14.5 16 L16 13.5 L21 15 L21 19 C21 20 20 21 19 21 C10 20.5 3.5 14 3 5 C3 4 4 3 5 3 Z"/></svg>
      <span style="font-weight:600">780XXXXXXX</span>
    </div>
    <div class="footer-contact" style="top:104px">
      <svg width="18" height="18" viewBox="0 0 24 24" fill="none" stroke="#fff" stroke-width="1.5"><rect x="2.5" y="5" width="19" height="14"/><path d="M2.5 5 L12 13 L21.5 5"/></svg>
      <span>info@brisbeckcurrentglide.example</span>
    </div>
    <div class="footer-contact" style="top:133px">
      <svg width="18" height="18" viewBox="0 0 24 24" fill="none" stroke="#fff" stroke-width="1.5"><path d="M12 21 C12 21 5 14 5 9 A7 7 0 0 1 19 9 C19 14 12 21 12 21 Z"/><circle cx="12" cy="9" r="2.5"/></svg>
      <span>4120 Ferrow Lane NW, Edmonton, AB</span>
    </div>
    <p class="abs" style="left:890px;top:165px;font-size:12px;color:var(--cyan);font-weight:300">Follow on Us:</p>
    <div class="footer-social" style="left:889px">Pix</div>
    <div class="footer-social" style="left:936px">Feed</div>
    <div class="footer-social" style="left:983px">Rate</div>

    <div class="footer-rule"></div>
    <p class="copyright">© 2022 BRISBECK CURRENT GLIDE. All rights reserved.</p>
  </footer>
</div>
</body>
</html>
```